Social Media designs (LinkedIn banner, LinkedIn posts, Instagram)

Hello designers!
We are looking to create some more concepts for our social media identity for a search firm (recruitment company)
I have attached a "brand toolkit" that shows our brand, logo, colour scheme to guide you with regards to colours and identiy.

You will see in the brand toolkit there are some examples of;
- A LinkedIn banner for the company (page 23)
- Social Media posts for LinkedIn and Instagram (page 21)

What we are looking for...

We don't really like the current LinkedIn banner ideas. We would like to see more concepts that look more aesthetically pleasing - the current ideas look quite dull.

We DO like the social media post concepts but we would like to have more templates/options that we can use (similar themes)

We welcome submissions for Social Media designs that we can use with our company branding. Thank you for your work in advance!

```html
<!DOCTYPE html>
<html lang="en">
<head>
<meta charset="utf-8">
<title>Harlow Reed – LinkedIn Banner</title>
<link rel="stylesheet" href="https://fonts.googleapis.com/css2?family=Figtree:wght@500&display=swap">
<style>
  :root {
    --page-grey: #b1b1b1;
    --forest-dark: #142725;
    --forest-mid: #2c6653;
    --forest-deep: #1c4639;
    --cream: #e6e4dc;
    --photo-light: #d9ddd6;
    --photo-mid: #a9b5a4;
    --photo-green: #7f9a7c;
  }
  html, body {
    margin: 0;
    padding: 0;
    width: 1200px;
    height: 1200px;
    overflow: hidden;
    background: var(--page-grey);
    font-family: "Figtree", sans-serif;
  }
  .stage {
    position: relative;
    width: 1200px;
    height: 1200px;
  }
  .banner {
    position: absolute;
    left: 68px;
    top: 427px;
    width: 1056px;
    height: 263px;
    box-shadow: 0 6px 10px rgba(0, 0, 0, 0.35);
    overflow: hidden;
  }
  .banner-art {
    position: absolute;
    inset: 0;
    width: 100%;
    height: 100%;
    display: block;
  }
  .brand-name {
    position: absolute;
    left: 25px;
    top: 24px;
    margin: 0;
    color: var(--cream);
    font-weight: 500;
    font-size: 20px;
    line-height: 21px;
  }
  .headline {
    position: absolute;
    left: 275px;
    top: 56px;
    margin: 0;
    color: var(--cream);
    font-weight: 500;
    font-size: 50px;
    line-height: 58px;
    letter-spacing: -0.3px;
  }
  .profile-badge {
    position: absolute;
    left: 96px;
    top: 608px;
    width: 142px;
    height: 142px;
    border-radius: 50%;
    background: var(--cream);
    box-shadow: 0 5px 9px rgba(0, 0, 0, 0.35);
    display: flex;
    align-items: center;
    justify-content: center;
    text-align: center;
    color: var(--forest-dark);
    font-weight: 500;
    font-size: 24px;
    line-height: 26px;
  }
</style>
</head>
<body>
  <div class="stage">
    <section class="banner">
      <svg class="banner-art" viewBox="0 0 1584 395" preserveAspectRatio="none">
        <defs>
          <linearGradient id="stripe-green" x1="0" y1="0" x2="0" y2="1">
            <stop offset="0" stop-color="var(--forest-mid)"/>
            <stop offset="1" stop-color="var(--forest-deep)"/>
          </linearGradient>
          <linearGradient id="photo-tone" x1="0" y1="0" x2="1" y2="1">
            <stop offset="0" stop-color="var(--photo-mid)"/>
            <stop offset="0.45" stop-color="var(--photo-light)"/>
            <stop offset="1" stop-color="var(--photo-green)"/>
          </linearGradient>
        </defs>
        <rect class="base" width="1584" height="395" fill="var(--forest-dark)"/>
        <polygon class="accent-band" points="0,318 878,318 1053,0 1138,0 922,395 0,395" fill="url(#stripe-green)"/>
        <polygon class="photo-area" points="1196,0 1584,0 1584,395 980,395" fill="url(#photo-tone)"
                 role="img" aria-label="Photo of a professional woman in a white blazer working on a laptop at a bright office desk"/>
      </svg>
      <p class="brand-name">Harlow<br>Reed</p>
      <h1 class="headline">Talents know<br>no borders</h1>
    </section>
    <div class="profile-badge">Harlow<br>Reed</div>
  </div>
</body>
</html>
```